Lirra - food stand (booth) design

We need posters for a small food stand situated in the centre of the city directly in front of a high-class shopping mall (see file 2 - the food stand at the square) . We sell cinnamon rolls which we named Lirra. We are looking for a design of the food stand which would lure the customer from the square in front of the mall of a size 30 meters (100 ft) wide. At the same time, it should be elegant, possibly Provence style in pastel colours.

We need the name and description of the product (meaning: Lirra – cinnamon rolls) to be visible from the front and maybe even the sides of the food stand. At the same time, we need to place the menu on some "wings", attached to the sides of the stand from outside. The menu will consist of 8 products (4 different kinds of Lirra rolls and 4 kinds of coffee). If you could visualize the wings, it would be nice.

We also need the design of the packaging of the product (a box similar to a hamburger box and a coffee cup) which might carry the logo (which we do not have), but again that is up to you. If you design the logo, maybe it should be placed on the outside of the food stand (up to you).

See the enclosed photos of the food stand from the front and the sides. The size of the food stand’s plan view is 2.5 x 2 meters (8.2 x 6.56 ft). The design can be either in the size of the current stickers (which would be replaced by yours) or it can cover the whole stand.

Below are sizes of the panels. We notice only the relevant ones
(for example the upper front is irrelevant, because it's always open, thus invisible). First is always x (eg. horizontal) axis. All sizes in centimeters.
A Front
A1 lower 234 x 40 cm
B Left side
B1 upper 174 x 100 cm
B2 lower 184 x 48 cm
C Right side (with the door)
C1 left 100 x 100 cm
C2 right (door) 48 x 184 cm

We are looking forward to your designs!

Thank you,
Team Lirra

```html
<!DOCTYPE html>
<html lang="en">
<head>
<meta charset="utf-8">
<title>Lirra Cinnamon Rolls &amp; Coffee – Stand Banner</title>
<link href="https://fonts.googleapis.com/css2?family=Oswald:wght@500&display=swap" rel="stylesheet">
<style>
  :root {
    --caramel-light: #e3a656;
    --caramel: #c98a3f;
    --caramel-deep: #9a5d27;
    --espresso: #3f1d0e;
    --espresso-mid: #5a2b16;
    --cream: #ecd3ad;
    --icing: #efe6d8;
    --cup: #8c6a45;
    --bean: #3a1a0c;
  }
  html, body {
    margin: 0;
    padding: 0;
    overflow: hidden;
    background: #ffffff;
  }
  .banner {
    position: relative;
    width: 1200px;
    height: 261px;
    overflow: hidden;
    background: radial-gradient(ellipse at 35% 55%, var(--caramel-light) 0%, var(--caramel) 40%, var(--caramel-deep) 100%);
  }
  .banner__dark-field {
    position: absolute;
    inset: 0;
    width: 1200px;
    height: 261px;
  }
  .product-roll,
  .product-cup,
  .cinnamon-chevron,
  .coffee-beans {
    position: absolute;
  }
  .product-roll {
    left: 44px;
    top: 44px;
    width: 216px;
    height: 168px;
    border-radius: 40% 40% 18% 18% / 30% 30% 14% 14%;
    background: linear-gradient(180deg, var(--icing) 0%, #e2c394 45%, #c8843f 100%);
  }
  .product-cup {
    left: 262px;
    top: 30px;
    width: 114px;
    height: 182px;
    border-radius: 10px 10px 16px 16px;
    background: linear-gradient(180deg, #f2f2f2 0%, #f2f2f2 16%, var(--cup) 16%, #6b4a2c 100%);
  }
  .cinnamon-chevron {
    left: 400px;
    top: 0;
    width: 230px;
    height: 261px;
  }
  .brand {
    position: absolute;
    left: 652px;
    top: 36px;
    width: 300px;
    display: flex;
    flex-direction: column;
    gap: 10px;
    color: var(--cream);
    font-family: "Oswald", "Arial Narrow", sans-serif;
    font-weight: 500;
  }
  .brand__name {
    margin: 0;
    font-size: 96px;
    line-height: 1;
    font-weight: 500;
    letter-spacing: 4px;
  }
  .brand__product {
    margin: 0;
    font-size: 30px;
    line-height: 1;
    font-weight: 500;
    letter-spacing: 3px;
    white-space: nowrap;
  }
  .tagline {
    position: absolute;
    left: 975px;
    top: 96px;
    margin: 0;
    color: var(--cream);
    font-family: "Oswald", "Arial Narrow", sans-serif;
    font-size: 40px;
    line-height: 1;
    font-weight: 500;
    letter-spacing: 2px;
    white-space: nowrap;
  }
  .coffee-beans {
    left: 912px;
    top: 212px;
    width: 288px;
    height: 49px;
    border-radius: 40px 40px 0 0;
    background: linear-gradient(180deg, #5a2a12 0%, var(--bean) 100%);
  }
</style>
</head>
<body>
  <main class="banner">
    <svg class="banner__dark-field" viewBox="0 0 1200 261" aria-hidden="true">
      <defs>
        <linearGradient id="espressoField" x1="0" y1="0" x2="1" y2="0.4">
          <stop offset="0" stop-color="#4a2211"/>
          <stop offset="0.6" stop-color="#5c2d17"/>
          <stop offset="1" stop-color="#43200f"/>
        </linearGradient>
      </defs>
      <polygon points="404,0 1200,0 1200,261 432,261 580,132" fill="url(#espressoField)"/>
    </svg>

    <div class="product-roll" role="img" aria-label="Photo of an iced cinnamon roll"></div>
    <div class="product-cup" role="img" aria-label="Illustration of a takeaway coffee cup with a brown sleeve"></div>

    <svg class="cinnamon-chevron" viewBox="0 0 230 261" role="img" aria-label="Cinnamon sticks arranged in an arrow shape">
      <polygon points="4,0 26,0 190,128 176,138" fill="#a4582b"/>
      <polygon points="176,134 190,128 42,261 28,261" fill="#93491f"/>
    </svg>

    <section class="brand">
      <h1 class="brand__name">LIRRA</h1>
      <p class="brand__product">CINNAMON ROLLS</p>
    </section>

    <p class="tagline">&amp; COFFEE</p>

    <div class="coffee-beans" role="img" aria-label="Pile of roasted coffee beans"></div>
  </main>
</body>
</html>
```